Bright Harbor Brochure/Flyer Revisions

Improve the current design and over all look for Tri-Fold brochure and 8 x 11 flyer along with update the text and view picture substitutions.

Target Market(s)

Currently our brochure is geared more towards the Cancer Patient, and less Senior.
I want to take the new revisions text, or new message, and incorporate it into the new designed brochure and flyer. I want a nice picture of a senior or couple to be primary view shot and the cancer patients secondary.
Please visit our website; www.brightharbors.org

Requirements
Must have
• we want all Seniors and Cancer Patients that own a life insurance policy, group or individual to call us. We want the consumer to be educated and know their rights.
Bright Harbors will be there ADVOCATE and Financial RESOURCE

```html
<!DOCTYPE html>
<html lang="en">
<head>
<meta charset="utf-8">
<title>Bright Harbors Brochure</title>
<link href="https://fonts.googleapis.com/css2?family=Arvo:wght@400;700&display=swap" rel="stylesheet">
<style>
  :root {
    --backdrop: #e4e4e4;
    --frame: #4f4c4c;
    --navy: #0b1a4a;
    --teal: #3ab0c2;
    --teal-light: #6cc8d6;
    --lime: #9bc53d;
    --slate: #5a5858;
    --white: #ffffff;
    --ink: #1b1b1b;
  }
  * { box-sizing: border-box; margin: 0; padding: 0; }
  html, body { width: 1200px; height: 899px; overflow: hidden; }
  body {
    background: var(--backdrop);
    font-family: "Arvo", Georgia, serif;
    position: relative;
  }
  .brochure {
    position: absolute;
    left: 60px; top: 90px;
    width: 1080px; height: 720px;
    display: flex;
    box-shadow: 0 10px 30px rgba(0,0,0,.18);
  }
  .panel {
    width: 360px; height: 720px;
    background: var(--frame);
    padding: 14px;
    position: relative;
  }
  .panel + .panel { border-left: 1px solid rgba(0,0,0,.25); }

  /* Panel: It's Your Money */
  .money { display: flex; flex-direction: column; }
  .money .photo-doctor {
    height: 210px;
    background: linear-gradient(135deg, #f1f3f5 0%, #d7e2ea 45%, #8fb0cf 70%, #ccd6de 100%);
  }
  .accent-bars { display: flex; height: 18px; }
  .accent-bars span { flex: 1; }
  .accent-bars .bar-slate { background: var(--slate); }
  .accent-bars .bar-teal { background: var(--teal); }
  .accent-bars .bar-lime { background: var(--lime); }
  .money .story {
    flex: 1;
    background: var(--navy);
    padding: 22px 22px 0;
    display: flex; flex-direction: column;
  }
  .money h2 {
    color: var(--teal);
    font-size: 27px;
    font-weight: 400;
    letter-spacing: .5px;
    margin-bottom: 10px;
  }
  .money .questions {
    color: var(--white);
    font-size: 12.5px;
    line-height: 1.45;
  }
  .money .questions p + p { margin-top: 4px; }
  .money .photo-couple {
    margin: 14px -22px 0;
    flex: 1;
    background: linear-gradient(160deg, #0b1a4a 0%, #3b3431 45%, #e8e6e4 70%, #1d1d1d 100%);
  }

  /* Panel: Everyone We Can Help */
  .help { display: flex; flex-direction: column; }
  .help .inner { flex: 1; background: var(--teal); display: flex; flex-direction: column; }
  .help .photo-care {
    height: 250px;
    background: linear-gradient(135deg, #dfe7ee 0%, #a9c4db 40%, #6b4a3c 75%, #9a7a6a 100%);
  }
  .help h2 {
    color: var(--white);
    font-weight: 400;
    font-size: 38px;
    line-height: 1.1;
    padding: 26px 24px 14px;
  }
  .help .intro {
    color: var(--white);
    font-size: 13px;
    line-height: 1.6;
    padding: 0 24px;
  }
  .help .intro + .intro { margin-top: 10px; }

  /* Panel: Reply card */
  .reply .inner {
    height: 100%;
    background: var(--teal);
    padding: 26px 24px 22px;
    color: var(--ink);
    display: flex; flex-direction: column;
  }
  .reply .request { font-size: 12px; line-height: 1.45; margin-bottom: 22px; }
  .field {
    display: flex; align-items: flex-end;
    font-size: 17px;
    height: 44px;
  }
  .field .line { flex: 1; border-bottom: 2px solid var(--white); margin-left: 8px; margin-bottom: 5px; }
  .field-pair { display: flex; gap: 12px; }
  .field-pair .field { flex: 1; }
  .reply .confidential {
    font-size: 15px;
    font-weight: 400;
    text-transform: uppercase;
    margin-top: 26px;
    line-height: 1.35;
  }
  .reply .disclaimer { font-size: 11px; margin-top: 10px; line-height: 1.4; }
  .reply .brand {
    margin-top: auto;
    align-self: flex-end;
    display: flex; align-items: center; gap: 8px;
    color: var(--navy);
    font-weight: 700;
    font-size: 17px;
  }
  .brand .mark { width: 14px; height: 14px; border-radius: 50%; background: var(--navy); }
</style>
</head>
<body>
  <div class="brochure">
    <section class="panel money">
      <div class="photo-doctor" role="img" aria-label="Photo of a doctor in a white coat with a stethoscope"></div>
      <div class="accent-bars"><span class="bar-slate"></span><span class="bar-teal"></span><span class="bar-lime"></span><span class="bar-teal"></span></div>
      <div class="story">
        <h2>It's Your Money.....</h2>
        <div class="questions">
          <p>Why do insurance companies conceal the fact that policy holders may be entitled to additional cash benefits?</p>
          <p>Why are bankruptcy rates among cancer patients and seniors more than double than that of the general population?</p>
          <p>Why do the majority of patients who are receiving care feel uncomfortable with discussing the subject of money and the overwhelming effects it has on the entire family?</p>
        </div>
        <div class="photo-couple" role="img" aria-label="Photo of a man embracing a woman undergoing cancer treatment"></div>
      </div>
    </section>

    <section class="panel help">
      <div class="inner">
        <div class="photo-care" role="img" aria-label="Photo of a doctor caring for a patient"></div>
        <h2>Everyone<br>We can Help</h2>
        <p class="intro">Whether you hold a group or individual policy, our advocates explain your options clearly and at no cost to you.</p>
        <p class="intro">Call today to learn more.</p>
      </div>
    </section>

    <section class="panel reply">
      <div class="inner">
        <p class="request">Yes, I would like more information about and the FREE REFERRAL SERVICE you offer to all patients</p>
        <div class="field">Name:<span class="line"></span></div>
        <div class="field">Address:<span class="line"></span></div>
        <div class="field">City:<span class="line"></span></div>
        <div class="field-pair">
          <div class="field">State:<span class="line"></span></div>
          <div class="field">Zip Code:<span class="line"></span></div>
        </div>
        <div class="field">E-mail address:<span class="line"></span></div>
        <div class="field">Phone :<span class="line"></span></div>
        <div class="field">Insurance Co.<span class="line"></span></div>
        <p class="confidential">All communication will be kept strictly confidential</p>
        <p class="disclaimer">Bright Harbors are not available to all patients and certain restriction may apply</p>
        <div class="brand"><span class="mark"></span>Bright Harbors</div>
      </div>
    </section>
  </div>
</body>
</html>
```